Alberta, Canada based Environmental Oilfield Consultant need a Business Card Design

We need a business card design for a year old company based in Edmonton, Alberta, Canada called Brambleton Consulting Inc. We are environmental consultants primarily for oilfield based companies (pipeline cleanup, site consultations, environmental site training, and site evaluations).

We like the color blue or green, something very clean and crisp looking.
We don't really care if there is an otter on it but most of our work is land based and nothing really to do with oceans or larger bodies of water.

The name Brambleton was the name of our fathers boat, and named our company that in his memory.

```html
<!DOCTYPE html>
<html lang="en">
<head>
<meta charset="utf-8">
<title>Brambleton Consulting Inc. – Business Card</title>
<link href="https://fonts.googleapis.com/css2?family=Exo+2:wght@400;500;700&display=swap" rel="stylesheet">
<style>
  :root {
    --stage: #e6e8ee;
    --card: #f7f8fa;
    --blue-deep: #3049ae;
    --blue-bright: #1a9be0;
    --brand: #1f78c8;
    --ink: #2a2c33;
    --white: #ffffff;
  }
  * { margin: 0; padding: 0; box-sizing: border-box; }
  html, body { width: 1200px; height: 840px; overflow: hidden; background: var(--stage); }
  .canvas { position: relative; width: 1200px; height: 840px; }
  .card {
    position: absolute; left: 75px; top: 120px; width: 1050px; height: 600px;
    background: var(--card); overflow: hidden;
    box-shadow: 0 10px 30px rgba(40, 50, 80, 0.18);
    font-family: "Exo 2", sans-serif;
  }
  .header-artwork {
    position: absolute; left: 0; top: 0; width: 100%; height: 190px;
    background: linear-gradient(90deg, var(--blue-deep) 0%, var(--blue-bright) 55%, var(--blue-deep) 100%);
  }
  .holder { position: absolute; top: 38px; right: 40px; text-align: right; color: var(--white); }
  .holder-name { font-size: 32px; font-weight: 500; letter-spacing: 2px; }
  .holder-title { font-size: 22px; font-weight: 400; letter-spacing: 0.5px; margin-top: 2px; }
  .brand { position: absolute; right: 60px; top: 262px; text-align: right; }
  .brand-name { font-size: 64px; font-weight: 700; line-height: 1; color: var(--brand); letter-spacing: 1px; }
  .address { margin-top: 20px; font-size: 25px; line-height: 1.25; color: var(--ink); letter-spacing: 1px; }
  .contacts { position: absolute; left: 50px; bottom: 40px; list-style: none; color: var(--ink); font-size: 20px; letter-spacing: 1px; }
  .contacts li { display: flex; align-items: center; gap: 14px; height: 31px; }
  .contacts svg { width: 20px; height: 20px; fill: var(--ink); flex: none; }
</style>
</head>
<body>
<div class="canvas">
  <section class="card" aria-label="Brambleton Consulting Inc. business card">
    <div class="header-artwork" role="img" aria-label="Blue wave artwork across the top of the card"></div>

    <header class="holder">
      <p class="holder-name">DANIEL HARTLEY</p>
      <p class="holder-title">Managing Director</p>
    </header>

    <div class="brand">
      <p class="brand-name">Brambleton<br>Consulting</p>
      <p class="address">410, 12th Floor, Kestrel<br>Whitemud Road NW</p>
    </div>

    <ul class="contacts">
      <li><svg viewBox="0 0 20 20"><path d="M5 2 L8 6 L6.5 8 C7.5 10.5 9.5 12.5 12 13.5 L14 12 L18 15 L16 18 C9 18 2 11 2 4 Z"/></svg>780 555 0142</li>
      <li><svg viewBox="0 0 20 20"><path d="M6 1 H14 A1.5 1.5 0 0 1 15.5 2.5 V17.5 A1.5 1.5 0 0 1 14 19 H6 A1.5 1.5 0 0 1 4.5 17.5 V2.5 A1.5 1.5 0 0 1 6 1 Z M6.5 3.5 V15 H13.5 V3.5 Z"/></svg>780 555 0143</li>
      <li><svg viewBox="0 0 20 20"><path d="M3 8 H17 V18 H3 Z M6 2 H14 V7 H6 Z"/></svg>780 555 0144</li>
      <li><svg viewBox="0 0 20 20"><path d="M2 4 H18 V16 H2 Z M3.5 5.5 L10 11 L16.5 5.5 V6.8 L10 12.5 L3.5 6.8 Z" fill-rule="evenodd"/></svg>info@brambletonci.ca</li>
      <li><svg viewBox="0 0 20 20"><path d="M10 1 A9 9 0 1 0 10.01 1 Z M3 10 H17 M10 2 C6 6 6 14 10 18 C14 14 14 6 10 2" fill="none" stroke="var(--ink)" stroke-width="1.6"/></svg>www.brambletonci.ca</li>
    </ul>
  </section>
</div>
</body>
</html>
```